PLUMBING POSTCARD DESIGN (MARKETING)

We are a local Plumbing business , Needing a post card to market domestic plumbing maintenance in my local area. The post card will have a magnet business card attached so allowance in design will need to be made. I have a slogan i want Incorporated into the design and is "TRY THE BEST, FLUSH THE REST"
I have attached my company name and logo to also incorporate into the design.
post card size 21cm L x 10cm H
business magnet card that will be attached to post card is 9cm L X 5.5cm H.
Post card will be one sided and will need following text inserted into design:
Pipevale would like to offer its fellow locals $40 off their next plumbing job. We pride ourselves in supplying the highest level of workmanship at the most competitive prices. CALL US TODAY
0431 582 907
Target Market(s)
Property owners (domestic market0
Industry/Entity Type
Plumbing
Requirements
Must have
- Eye catching, Slogan, company name and logo

```html
<!DOCTYPE html>
<html lang="en">
<head>
<meta charset="utf-8">
<title>Pipevale Postcard</title>
<link href="https://fonts.googleapis.com/css2?family=Roboto:wght@400;500;700;900&display=swap" rel="stylesheet">
<style>
  :root{
    --page:#d3dce4;
    --orange:#f07138;
    --blue:#2a8bbd;
    --blue-bright:#22a9d6;
    --blue-deep:#2a7fae;
    --ink:#3a3a3a;
    --grey:#6d6d6d;
    --white:#ffffff;
    --tick:#f0a030;
  }
  *{margin:0;padding:0;box-sizing:border-box}
  html,body{width:1200px;height:1200px;overflow:hidden;background:var(--page);font-family:'Roboto',Arial,sans-serif}
  .canvas{position:relative;width:1200px;height:1200px}
  .card{position:absolute;overflow:hidden;background:var(--white);box-shadow:4px 6px 10px rgba(0,0,0,.25)}
  .abs{position:absolute}
  .bg{position:absolute;left:0;top:0}
  .center{text-align:center;transform:translateX(-50%)}

  /* wide banner */
  .wide{left:50px;top:51px;width:1100px;height:523px}
  .wide > .banner-headline{left:0;top:28px;width:690px;text-align:center;color:var(--white);font-weight:900;font-size:64px;line-height:67px;letter-spacing:-.5px}
  .wide > .banner-offer{left:30px;top:192px;width:530px;text-align:center;color:var(--ink);font-size:22px;line-height:37px}
  .wide > .banner-offer b{color:var(--blue-bright);font-weight:500}
  .wide > .banner-slogan{left:294px;top:350px;white-space:nowrap;color:var(--blue-bright);font-weight:700;font-size:32px}
  .wide > .banner-call{left:294px;top:388px;white-space:nowrap;color:var(--orange);font-weight:700;font-size:58px;display:flex;align-items:center;gap:14px}
  .wide > .banner-number{left:294px;top:450px;white-space:nowrap;color:var(--blue-deep);font-weight:500;font-size:52px;letter-spacing:.3em}
  .wide > .banner-url{left:678px;top:450px;color:var(--white);font-size:33px;letter-spacing:3.5px}
  .wide > .magnet{left:613px;top:133px;width:850px;height:519px;transform:scale(.554);transform-origin:0 0;box-shadow:none}

  /* postcard layout (used full size and as the magnet card) */
  .postcard{left:178px;top:629px;width:850px;height:519px}
  .pc .headline{left:228px;top:20px;white-space:nowrap;color:var(--white);font-weight:700;font-size:52px;line-height:60px;letter-spacing:-.5px}
  .pc .pill{left:44px;top:154px;width:362px;height:62px;border:2px solid var(--white);border-radius:31px;background:var(--blue-bright);color:var(--white);font-size:22px;line-height:24px;font-weight:500;text-align:center;display:flex;align-items:center;justify-content:center}
  .pc .amount{left:225px;top:224px;white-space:nowrap;color:var(--white);font-weight:700;font-size:82px;line-height:100px}
  .pc .job{left:225px;top:316px;white-space:nowrap;color:var(--white);font-weight:700;font-size:22px}
  .pc .call{left:225px;top:379px;white-space:nowrap;color:var(--white);font-weight:700;font-size:42px;line-height:50px}
  .pc .phone{left:30px;top:446px;white-space:nowrap;color:var(--white);font-weight:700;font-size:52px;line-height:60px;display:flex;align-items:center;gap:14px}
  .pc .brand{left:520px;top:34px;display:flex;align-items:center;gap:12px}
  .pc .brand-dot{width:44px;height:44px;border-radius:50%;background:var(--blue-bright)}
  .pc .brand-name{font-weight:700;font-size:40px;line-height:40px;color:#4a4a4a}
  .pc .brand-sub{left:586px;top:76px;font-size:17px;color:var(--grey);letter-spacing:.3px;white-space:nowrap}
  .pc .photo{left:498px;top:131px}
  .pc .services{left:466px;top:270px;list-style:none}
  .pc .services li{display:flex;align-items:center;gap:10px;height:26.6px;font-size:18px;font-weight:500;color:#3d3d3d;white-space:nowrap}
  .pc .contact{left:486px;top:442px;color:var(--white);font-size:16px;font-weight:700;line-height:23.5px;white-space:nowrap}
  .pc .contact div{display:flex;align-items:center;gap:9px}
  .pc .divider{left:697px;top:444px;width:2px;height:64px;background:#f3b23c}
  .pc .follow{left:773px;top:446px;color:var(--white);font-size:17px;font-weight:500;letter-spacing:3px;white-space:nowrap}
  .pc .social{top:477px;width:28px;height:28px;border-radius:50%;background:#f3a534}
</style>
</head>
<body>
<div class="canvas">

  <!-- wide banner -->
  <section class="card wide">
    <svg class="bg" width="1100" height="523" viewBox="0 0 1100 523">
      <path d="M762 0 H1100 V523 H534 C610 470 660 430 690 390 L690 230 C692 150 720 60 762 0 Z" fill="var(--blue)"/>
      <path d="M0 0 H738 C670 60 630 120 590 149 C560 170 540 179 500 181 L0 184 Z" fill="var(--orange)"/>
    </svg>
    <div class="abs banner-headline">TRY THE BEST,<br>FLUSH THE REST</div>
    <p class="abs banner-offer">Pipevale would like to offer its fellow locals <b>$40 OFF</b> their next plumbing job. We pride ourselves in supplying the highest level of workmanship at the most competitive prices.</p>
    <div class="abs banner-slogan center">TRY THE BEST, FLUSH THE REST</div>
    <div class="abs banner-call center">
      <svg width="46" height="46" viewBox="0 0 46 46" fill="none" stroke="var(--orange)" stroke-width="4"><circle cx="23" cy="23" r="20"/><path d="M15 13 l5 -1 3 6 -3 3 c2 4 4 6 7 8 l3 -3 6 3 -1 5 c-12 0 -20 -9 -20 -21z" fill="var(--orange)" stroke="none"/></svg>
      CALL US TODAY
    </div>
    <div class="abs banner-number center">0431 582 907</div>
    <div class="abs banner-url">www.pipevale.com.au</div>

    <section class="card abs magnet pc" aria-hidden="true">
      <svg class="bg" width="850" height="519" viewBox="0 0 850 519">
        <defs>
          <linearGradient id="warmA" x1="0" y1="0" x2="0" y2="1"><stop offset="0" stop-color="#f6b23c"/><stop offset="1" stop-color="#f07f30"/></linearGradient>
          <clipPath id="leftA"><path d="M0 0 H462 C500 60 500 180 480 240 C450 330 400 380 420 440 C425 470 440 500 452 519 H0 Z"/></clipPath>
        </defs>
        <rect x="400" y="435" width="450" height="84" fill="var(--blue-bright)"/>
        <path d="M0 0 H484 C522 60 522 180 502 240 C472 330 422 380 442 440 C447 470 462 500 474 519 H0 Z" fill="var(--blue)"/>
        <g clip-path="url(#leftA)">
          <rect width="500" height="373" fill="url(#warmA)"/>
          <rect y="373" width="500" height="62" fill="var(--blue)"/>
          <rect y="435" width="500" height="84" fill="var(--orange)"/>
        </g>
      </svg>
      <div class="abs headline center">TRY THE BEST,<br>FLUSH THE REST</div>
      <div class="abs pill">PIPEVALE WOULD LIKE TO<br>OFFER ITS FELLOW LOCALS</div>
      <div class="abs amount center">$40 OFF</div>
      <div class="abs job center">THEIR NEXT PLUMBING JOB.</div>
      <div class="abs call center">CALL US TODAY</div>
      <div class="abs phone"><svg width="50" height="50" viewBox="0 0 46 46" fill="none" stroke="#fff" stroke-width="4"><circle cx="23" cy="23" r="20"/><path d="M15 13 l5 -1 3 6 -3 3 c2 4 4 6 7 8 l3 -3 6 3 -1 5 c-12 0 -20 -9 -20 -21z" fill="#fff" stroke="none"/></svg>0431 582 907</div>
      <div class="abs brand"><span class="brand-dot"></span><span class="brand-name">PIPEVALE</span></div>
      <div class="abs brand-sub">PLUMBING | DRAINAGE | GAS</div>
      <svg class="abs photo" width="336" height="304" viewBox="0 0 336 304"><path d="M0 0 H336 V304 H196 V139 H0 Z" fill="#c9d2da"/></svg>
      <ul class="abs services">
        <li><svg width="13" height="13" viewBox="0 0 13 13" fill="none" stroke="var(--tick)" stroke-width="1.6"><rect x="1" y="1" width="11" height="11"/><path d="M3 6.5 l2.5 2.5 5 -6"/></svg>New Homes</li>
        <li><svg width="13" height="13" viewBox="0 0 13 13" fill="none" stroke="var(--tick)" stroke-width="1.6"><rect x="1" y="1" width="11" height="11"/><path d="M3 6.5 l2.5 2.5 5 -6"/></svg>Bathroom Renovations</li>
        <li><svg width="13" height="13" viewBox="0 0 13 13" fill="none" stroke="var(--tick)" stroke-width="1.6"><rect x="1" y="1" width="11" height="11"/><path d="M3 6.5 l2.5 2.5 5 -6"/></svg>Kitchen Renovations</li>
        <li><svg width="13" height="13" viewBox="0 0 13 13" fill="none" stroke="var(--tick)" stroke-width="1.6"><rect x="1" y="1" width="11" height="11"/><path d="M3 6.5 l2.5 2.5 5 -6"/></svg>Plumbing Designs</li>
        <li><svg width="13" height="13" viewBox="0 0 13 13" fill="none" stroke="var(--tick)" stroke-width="1.6"><rect x="1" y="1" width="11" height="11"/><path d="M3 6.5 l2.5 2.5 5 -6"/></svg>Drainage Solutions</li>
        <li><svg width="13" height="13" viewBox="0 0 13 13" fill="none" stroke="var(--tick)" stroke-width="1.6"><rect x="1" y="1" width="11" height="11"/><path d="M3 6.5 l2.5 2.5 5 -6"/></svg>Gas Certification</li>
      </ul>
      <div class="abs contact">
        <div><svg width="16" height="16" viewBox="0 0 16 16" fill="#fff"><path d="M3 2 l3 -1 2 4 -2 2 c1 2 2 3 4 4 l2 -2 4 2 -1 3 c-8 0 -12 -5 -12 -12z"/></svg>hello@pipevale.com.au</div>
        <div><svg width="16" height="16" viewBox="0 0 16 16" fill="none" stroke="#fff" stroke-width="1.5"><circle cx="8" cy="8" r="6.5"/><path d="M1.5 8 H14.5 M8 1.5 C4 5 4 11 8 14.5 C12 11 12 5 8 1.5"/></svg>www.pipevale.com.au</div>
        <div><svg width="16" height="16" viewBox="0 0 16 16" fill="#fff"><rect x="1" y="4" width="14" height="10" rx="1"/><rect x="5" y="1.5" width="6" height="3" fill="none" stroke="#fff" stroke-width="1.5"/></svg>ABN: 41 208 377 152</div>
      </div>
      <div class="abs divider"></div>
      <div class="abs follow center">follow us</div>
      <span class="abs social" style="left:736px"></span>
      <span class="abs social" style="left:779px"></span>
    </section>
  </section>

  <!-- postcard -->
  <section class="card postcard pc">
    <svg class="bg" width="850" height="519" viewBox="0 0 850 519">
      <defs>
        <linearGradient id="warm" x1="0" y1="0" x2="0" y2="1"><stop offset="0" stop-color="#f6b23c"/><stop offset="1" stop-color="#f07f30"/></linearGradient>
        <clipPath id="leftPanel"><path d="M0 0 H462 C500 60 500 180 480 240 C450 330 400 380 420 440 C425 470 440 500 452 519 H0 Z"/></clipPath>
      </defs>
      <rect x="400" y="435" width="450" height="84" fill="var(--blue-bright)"/>
      <path d="M0 0 H484 C522 60 522 180 502 240 C472 330 422 380 442 440 C447 470 462 500 474 519 H0 Z" fill="var(--blue)"/>
      <g clip-path="url(#leftPanel)">
        <rect width="500" height="373" fill="url(#warm)"/>
        <rect y="373" width="500" height="62" fill="var(--blue)"/>
        <rect y="435" width="500" height="84" fill="var(--orange)"/>
      </g>
    </svg>
    <div class="abs headline center">TRY THE BEST,<br>FLUSH THE REST</div>
    <div class="abs pill">PIPEVALE WOULD LIKE TO<br>OFFER ITS FELLOW LOCALS</div>
    <div class="abs amount center">$40 OFF</div>
    <div class="abs job center">THEIR NEXT PLUMBING JOB.</div>
    <div class="abs call center">CALL US TODAY</div>
    <div class="abs phone"><svg width="50" height="50" viewBox="0 0 46 46" fill="none" stroke="#fff" stroke-width="4"><circle cx="23" cy="23" r="20"/><path d="M15 13 l5 -1 3 6 -3 3 c2 4 4 6 7 8 l3 -3 6 3 -1 5 c-12 0 -20 -9 -20 -21z" fill="#fff" stroke="none"/></svg>0431 582 907</div>
    <div class="abs brand"><span class="brand-dot"></span><span class="brand-name">PIPEVALE</span></div>
    <div class="abs brand-sub">PLUMBING | DRAINAGE | GAS</div>
    <svg class="abs photo" width="336" height="304" viewBox="0 0 336 304" role="img" aria-label="Photo of a white company van with a smiling plumber in a hard hat carrying toolboxes"><path d="M0 0 H336 V304 H196 V139 H0 Z" fill="#c9d2da"/></svg>
    <ul class="abs services">
      <li><svg width="13" height="13" viewBox="0 0 13 13" fill="none" stroke="var(--tick)" stroke-width="1.6"><rect x="1" y="1" width="11" height="11"/><path d="M3 6.5 l2.5 2.5 5 -6"/></svg>New Homes</li>
      <li><svg width="13" height="13" viewBox="0 0 13 13" fill="none" stroke="var(--tick)" stroke-width="1.6"><rect x="1" y="1" width="11" height="11"/><path d="M3 6.5 l2.5 2.5 5 -6"/></svg>Bathroom Renovations</li>
      <li><svg width="13" height="13" viewBox="0 0 13 13" fill="none" stroke="var(--tick)" stroke-width="1.6"><rect x="1" y="1" width="11" height="11"/><path d="M3 6.5 l2.5 2.5 5 -6"/></svg>Kitchen Renovations</li>
      <li><svg width="13" height="13" viewBox="0 0 13 13" fill="none" stroke="var(--tick)" stroke-width="1.6"><rect x="1" y="1" width="11" height="11"/><path d="M3 6.5 l2.5 2.5 5 -6"/></svg>Plumbing Designs</li>
      <li><svg width="13" height="13" viewBox="0 0 13 13" fill="none" stroke="var(--tick)" stroke-width="1.6"><rect x="1" y="1" width="11" height="11"/><path d="M3 6.5 l2.5 2.5 5 -6"/></svg>Drainage Solutions</li>
      <li><svg width="13" height="13" viewBox="0 0 13 13" fill="none" stroke="var(--tick)" stroke-width="1.6"><rect x="1" y="1" width="11" height="11"/><path d="M3 6.5 l2.5 2.5 5 -6"/></svg>Gas Certification</li>
    </ul>
    <div class="abs contact">
      <div><svg width="16" height="16" viewBox="0 0 16 16" fill="#fff"><path d="M3 2 l3 -1 2 4 -2 2 c1 2 2 3 4 4 l2 -2 4 2 -1 3 c-8 0 -12 -5 -12 -12z"/></svg>hello@pipevale.com.au</div>
      <div><svg width="16" height="16" viewBox="0 0 16 16" fill="none" stroke="#fff" stroke-width="1.5"><circle cx="8" cy="8" r="6.5"/><path d="M1.5 8 H14.5 M8 1.5 C4 5 4 11 8 14.5 C12 11 12 5 8 1.5"/></svg>www.pipevale.com.au</div>
      <div><svg width="16" height="16" viewBox="0 0 16 16" fill="#fff"><rect x="1" y="4" width="14" height="10" rx="1"/><rect x="5" y="1.5" width="6" height="3" fill="none" stroke="#fff" stroke-width="1.5"/></svg>ABN: 41 208 377 152</div>
    </div>
    <div class="abs divider"></div>
    <div class="abs follow center">follow us</div>
    <span class="abs social" style="left:736px"></span>
    <span class="abs social" style="left:779px"></span>
  </section>

</div>
</body>
</html>
```